Orsabellitravel.com web design project + logo design

Hi,

We are a Russian online tour operator - tripwelder.com

We are looking to tranmsfer our domain to orsabellitravel.com. The website and logo need to be orsabelliesque - we are not looking to change our functionality, but we need to make the website much more attracitve to clients, much more wild looking but at the same time remaining a professional travel company.

The main concept of the website should be innovative travel (as orsabelli was an innovator). Alternatively, you could go down the artist route and go down the draw / design your own tour road.

On our website the customer is able to combine travel services (hotels, flights, Visa services, and soon chauffeur, car rental etc...) put it into their basket (the basket definitely has to look better than it is at the moment) and pay for it in one go by card.

We are also stressin our customer support with web chat, call centre etc... (call centre number at the top of the page)

We aim to provide an easy user experience, but we need to make it have some more style, so I will be waiting for what you guys can come up with.
Let me know if you have any questions - skype is: mrkolbuzov

It Company

• It is quite a simple task - to take the existing website tripwelder.com and orsabellisize it to create orsabellitravel.com, the functionality of the website will remain the same and there are not many pages in the website. Homepage, Checkout step1, Checkout step 2 (you can view both of these if you select a service) and the generic pages for T&C''s, Privacy policy etc...

IMPORTANT UPDATE

We are also looking at how the search results will look in the designs, (please do a search on our website for hotel / flight)

```html
<!DOCTYPE html>
<html lang="ru">
<head>
<meta charset="utf-8">
<title>Orsabellitravel.com</title>
<link href="https://fonts.googleapis.com/css2?family=Arimo:wght@400;700&display=swap" rel="stylesheet">
<style>
:root{
  --teal:#0d5468;
  --teal-dark:#0a4656;
  --sky:#1ba3e0;
  --sky-light:#5fc8f5;
  --text:#1b1b1b;
  --white:#ffffff;
  --red:#c4223a;
  --pink:#e0506e;
  --grey:#5a5a5a;
  --field:#dfe4ee;
}
*{box-sizing:border-box;margin:0;padding:0}
html,body{width:1200px;height:900px;overflow:hidden}
body{position:relative;font-family:Arimo,Arial,sans-serif;color:var(--text);background:#fff}
.abs{position:absolute}
.site-header{left:0;top:0;width:1200px;height:100px;background:linear-gradient(#ffffff,#dfe6f3 60%,#b9c8e2)}
.header-rule{left:0;top:100px;width:1200px;height:5px;background:var(--sky)}
.brand{left:197px;top:38px;display:flex;align-items:center;gap:10px;font-size:24px;font-weight:700;color:#1a9bd6}
.brand-dot{width:22px;height:22px;border-radius:50%;background:#1a9bd6}
.hotlines{right:510px;top:18px;text-align:right;color:#f4f7fc;font-size:15px;line-height:23px;text-shadow:0 0 2px #8aa}
.nav-tab{top:0;height:100px;width:101px;border-left:1px solid #8aa;border-right:1px solid #8aa;text-align:center;font-size:9px;font-weight:700;color:#f0f3f8;text-shadow:0 0 2px #666}
.nav-tab svg{display:block;margin:20px auto 6px}
.nav-tab.active{background:linear-gradient(#3aa8e8,#1c86cc)}
.hero{left:0;top:105px;width:1200px;height:627px;background:linear-gradient(#4d79a6 0%,#a7c1d8 35%,#dbe6ef 65%,#60786e 75%,#4e6358 100%)}
.booking-frame{left:187px;top:238px;width:828px;height:339px;border-radius:12px;background:var(--teal)}
.booking-inner{left:198px;top:245px;width:807px;height:325px;background:linear-gradient(#e3e7ee,#c9cfd8);border-radius:4px}
.search-form{left:205px;top:258px;width:528px;height:299px;background:linear-gradient(#f8f9fb,#e1e5ec);border:1px solid #b9c0cc}
.tab{color:#fff;border-radius:3px;background:linear-gradient(#4fb7ef,#1579bf);text-align:center}
.tab-main{left:216px;top:255px;width:85px;height:28px;font-size:14px;line-height:28px}
.tab-alt{left:318px;top:256px;width:60px;height:20px;font-size:10px;line-height:18px}
.label{font-size:14px}
.field{height:28px;border-radius:4px;background:linear-gradient(#f4f6fa,#d3dae6);border:1px solid #c8cfdb}
.select{height:25px;border:1px solid #9aa3b0;border-radius:4px;background:linear-gradient(#fff,#e6e9ef)}
.select::after{content:"";position:absolute;right:7px;top:6px;border:8px solid transparent;border-top:11px solid var(--red);border-bottom:0}
.check{font-size:9px;display:flex;align-items:center;gap:3px}
.check i{width:13px;height:11px;border:1px solid #888;background:#fff;border-radius:2px;display:inline-block;font-style:normal;font-size:11px;line-height:9px;font-weight:700}
.submit{left:598px;top:499px;width:97px;height:30px;border-radius:3px;background:linear-gradient(#e05567,#a6132a);color:#fff;font-size:14px;text-align:center;line-height:30px;box-shadow:0 4px 4px -2px #777}
.cart-head{left:733px;top:259px;width:264px;height:52px;border-radius:10px;background:linear-gradient(#fff,#c8cfdc);border:1px solid #aab;font-size:18px;text-align:center;line-height:48px}
.cart-visual{left:733px;top:319px;width:262px;height:118px;background:linear-gradient(#e8587a,#b51d40)}
.cart-bar{left:733px;top:437px;width:262px;height:23px;background:linear-gradient(90deg,#1aa6e8,#9fe4ff 50%,#1aa6e8);text-align:center;font-size:14px;line-height:22px}
.cart-body{left:733px;top:460px;width:262px;height:95px;background:var(--grey)}
.cart-status{left:733px;top:464px;width:262px;text-align:center;color:#fff;font-size:16px;font-weight:700}
.pay{left:735px;top:489px;width:258px;height:37px;border-radius:6px;background:linear-gradient(#fff,#cfd3da);text-align:center;line-height:37px;font-size:14px;color:#444}
.pricing{left:733px;top:534px;width:262px;text-align:center;color:#bbb;font-size:11px}
.footer-rim{left:0;top:732px;width:1200px;height:14px;background:linear-gradient(#f3f6fb,#9eb4c6)}
.site-footer{left:0;top:746px;width:1200px;height:154px;background:var(--teal)}
.footer-col{color:#fff;font-size:14px;line-height:18px}
.footer-col h3{font-weight:400;font-size:14px;margin-bottom:18px}
.contact{left:790px;top:757px;color:#fff;font-size:15px;line-height:22.5px}
.contact div{display:flex;align-items:center;gap:8px}
.email-box{left:817px;top:830px;width:104px;height:19px;background:var(--sky);border-radius:3px;color:#cfe9f7;font-size:10px;padding:3px 11px}
.email-go{left:925px;top:830px;width:70px;height:19px;background:var(--sky);border-radius:3px}
.privacy-note{left:816px;top:851px;color:#fff;font-size:9px;font-weight:700;line-height:11px}
</style>
</head>
<body>
<header class="abs site-header"></header>
<div class="abs header-rule"></div>
<div class="abs brand"><span class="brand-dot"></span>Orsabellitravel.com</div>
<div class="abs hotlines">1-800-555-0147<br>+1 (555) 010-42-86<br>(Пн-Пт) Часы работы: с 9:00 - до 18:00</div>
<nav>
  <div class="abs nav-tab" style="left:710px"><svg width="42" height="30" viewBox="0 0 42 30"><ellipse cx="14" cy="12" rx="13" ry="10" fill="#2ea4e6"/><ellipse cx="28" cy="15" rx="12" ry="9" fill="#f2a52b"/></svg>ФОРУМ</div>
  <div class="abs nav-tab" style="left:810px"><svg width="40" height="26" viewBox="0 0 40 26"><rect width="40" height="9" fill="#fff" stroke="#ccc"/><rect y="9" width="40" height="8" fill="#2a49b8"/><rect y="17" width="40" height="9" fill="#d42030"/></svg>ЯЗЫК</div>
  <div class="abs nav-tab active" style="left:910px"><svg width="40" height="30" viewBox="0 0 40 30"><circle cx="20" cy="10" r="8" fill="#333"/><path d="M4 30 Q20 12 36 30Z" fill="#333"/></svg>МОЙ ТУР</div>
</nav>
<div class="abs hero" role="img" aria-label="Панорама города с небоскрёбами, рекой и облачным небом"></div>

<div class="abs booking-frame"></div>
<div class="abs booking-inner"></div>
<form class="abs search-form"></form>
<div class="abs tab tab-main">Option 1</div>
<div class="abs tab tab-alt">Option 2</div>

<span class="abs label" style="left:218px;top:312px">Откуда</span>
<div class="abs field" style="left:293px;top:308px;width:139px"></div>
<span class="abs label" style="left:478px;top:312px">Куда</span>
<div class="abs field" style="left:541px;top:305px;width:139px"></div>
<span class="abs label" style="left:218px;top:368px">Туда</span>
<div class="abs field" style="left:293px;top:361px;width:103px"></div>
<span class="abs label" style="left:462px;top:368px">Обратно</span>
<div class="abs field" style="left:541px;top:361px;width:102px"></div>
<div class="abs check" style="left:646px;top:363px"><i></i>Обратно</div>
<div class="abs check" style="left:646px;top:376px"><i>✓</i>В одну сторону</div>
<span class="abs label" style="left:218px;top:422px">Пассажиры</span>
<svg class="abs" style="left:293px;top:417px" width="13" height="24" viewBox="0 0 13 24"><circle cx="6.5" cy="3" r="3" fill="#222"/><rect x="2" y="7" width="9" height="10" rx="2" fill="#222"/><rect x="3" y="15" width="3" height="9" fill="#222"/><rect x="7" y="15" width="3" height="9" fill="#222"/></svg>
<div class="abs select" style="left:309px;top:417px;width:62px"></div>
<svg class="abs" style="left:418px;top:422px" width="10" height="18" viewBox="0 0 10 18"><circle cx="5" cy="2.5" r="2.5" fill="#222"/><rect x="1.5" y="5.5" width="7" height="7" rx="1.5" fill="#222"/><rect x="2" y="11" width="2.5" height="7" fill="#222"/><rect x="5.5" y="11" width="2.5" height="7" fill="#222"/></svg>
<div class="abs select" style="left:430px;top:417px;width:62px"></div>
<div class="abs select" style="left:544px;top:417px;width:62px"></div>
<span class="abs label" style="left:218px;top:466px">Класс</span>
<div class="abs select" style="left:293px;top:462px;width:120px"></div>
<div class="abs submit">Submit</div>

<div class="abs cart-head">Корзина</div>
<div class="abs cart-visual">
  <svg style="position:absolute;left:88px;top:30px" width="70" height="80" viewBox="0 0 70 80"><path d="M4 6h12l10 48h36" fill="none" stroke="#fff" stroke-width="5" stroke-linecap="round"/><path d="M18 20h48l-6 28H24z" fill="none" stroke="#fff" stroke-width="4"/><circle cx="30" cy="68" r="6" fill="#fff"/><circle cx="56" cy="68" r="6" fill="#fff"/></svg>
</div>
<div class="abs cart-bar">▼</div>
<div class="abs cart-body"></div>
<div class="abs cart-status">пусто</div>
<div class="abs pay">Оплата</div>
<div class="abs pricing">* Ценовая политика</div>

<div class="abs footer-rim"></div>
<footer class="abs site-footer"></footer>
<div class="abs footer-col" style="left:184px;top:769px"><h3>Просмотр Сайта</h3>Домой<br>О нас<br>Форум<br>Контакты</div>
<div class="abs footer-col" style="left:336px;top:769px"><h3>Помощь</h3>Помощь<br>Правила пользования<br>Политика конфиденциальности<br>Cookies</div>
<div class="abs footer-col" style="left:595px;top:769px"><h3>Найти нас</h3>Trip Welder Limited<br>14 Marlow Lane<br>London, N4 7QT<br>UK</div>
<div class="abs contact">
  <div><svg width="17" height="14" viewBox="0 0 17 14"><path d="M2 5Q8.5-1 15 5l-3 2-2-2H7L5 7z" fill="#5bc0f0"/><rect x="4" y="8" width="9" height="5" rx="1" fill="#5bc0f0"/></svg>+7 (555) 013-27-64</div>
  <div><svg width="17" height="12" viewBox="0 0 17 12"><rect width="17" height="12" fill="#e8eef2"/><path d="M0 0l8.5 7L17 0" fill="none" stroke="#999"/></svg>info@tripwelder.com</div>
  <div><svg width="15" height="15" viewBox="0 0 15 15"><rect width="15" height="15" rx="2" fill="#f08a1c"/><circle cx="4" cy="11" r="1.6" fill="#fff"/><path d="M3 7a5 5 0 015 5M3 3.5A8.5 8.5 0 0111.5 12" fill="none" stroke="#fff" stroke-width="1.6"/></svg>Эксклюзивные предложения</div>
</div>
<div class="abs email-box">Email</div>
<div class="abs email-go"></div>
<div class="abs privacy-note">Ваши данные в безопасности, прочтите<br>нашу Политику Конфиденциальности</div>
</body>
</html>
```